VORELT B2B portal design
Fantastic design work, top communication and fast design changes! Many thanks,Jens & Uwe from VORELT
Zielgruppe
We are a B2B Cloud Services StartUp that creates B2B logistics & supply chain processes between customer and its suppliers.
Aufgabenstellung
We need a modern responsive able design, that should consider that we are NOT presenting goods or clothes or similar on the portal pages but we show mainly data grids, kpi dashboards, forms, and setting panels to our customer and their suppliers.
The design must be clean and straight not to distract people from the important information in these data grids, kpi dashboards, forms, and settings panels.
We need our logo perfectly embedded and the pages coloured around from grey to blue.
The Designer must be able to deliver a design and transfer it to a highly responsive HTML (5) template (without technical content or further functionality). This our programmers will implement afterwards in .Net.
We need in total 3 page templates:
1. Login Page
2. Main Page with overview over the following services text (each one shown in one tile)
"ZMS (Time Frame Management)"
"DMS (Document Management)"
"REMS (Reporting Management)"
-> Note: At the end we will have up to 12 or more tiles (services) so the design should be additive
3. Data grid (e.g. list of customers)/form (e.g. customer registration form) page to show some data grid with database data
See samples for each page enclosed!!

```html
<!DOCTYPE html>
<html lang="en">
<head>
<meta charset="utf-8">
<title>VORELT – Dashboard</title>
<link rel="stylesheet" href="https://fonts.googleapis.com/css2?family=Ubuntu:wght@400;500;700&display=swap">
<style>
:root{
  --navy:#0c2c44;
  --ink:#1d2f3e;
  --text:#4a4f55;
  --muted:#6b7076;
  --header-bg:#e1e6ea;
  --sidebar-bg:#e1e6ea;
  --page-bg:#f7f8fa;
  --line:#c9cfd4;
  --head-cell:#e1e6ea;
  --stripe:#eef6fb;
  --white:#ffffff;
  --chip:#b5b8bb;
}
*{box-sizing:border-box;margin:0;padding:0}
html,body{width:1200px;height:948px;overflow:hidden}
body{font-family:"Ubuntu",sans-serif;background:var(--page-bg);color:var(--text);position:relative}

.top-bar{position:absolute;left:0;top:0;width:1200px;height:137px;background:var(--header-bg);border-bottom:1px solid #b9c2ca}
.brand{position:absolute;left:20px;top:44px;display:flex;align-items:center;gap:12px}
.brand-dot{width:34px;height:34px;border-radius:50%;background:var(--navy)}
.brand-name{font-size:40px;font-weight:700;color:var(--navy);letter-spacing:1px}
.account{position:absolute;right:14px;top:36px;display:flex;align-items:center}
.account-text{text-align:right;margin-right:12px}
.account-name{font-size:20px;font-weight:500;color:var(--ink)}
.account-role{font-size:14px;color:var(--muted);margin-top:1px}
.avatar{width:66px;height:66px;border-radius:50%;background:radial-gradient(circle at 50% 40%,#9a948d,#4a4744);border:2px solid #f2f2f2}
.caret{margin-left:10px;width:0;height:0;border-left:5px solid transparent;border-right:5px solid transparent;border-top:6px solid #777}

.side-nav{position:absolute;left:0;top:137px;width:264px;height:710px;background:var(--sidebar-bg)}
.nav-item{display:flex;align-items:center;height:61px;padding-left:18px;font-size:20px;color:var(--ink);border-bottom:1px solid #c5ccd2}
.nav-item svg{width:28px;height:28px;margin-right:11px;fill:none;stroke:var(--ink);stroke-width:2}
.nav-item.active{background:var(--navy);color:var(--white);height:55px;border-bottom:none}
.nav-item.active svg{stroke:var(--white)}
.nav-item.plain{border-bottom:none}

.section-title{position:absolute;left:304px;font-size:24px;color:var(--ink);font-weight:400}

.data-grid{position:absolute;left:304px;top:228px;width:870px;border:1px solid var(--line);background:var(--white)}
.data-grid table,.simple-table table{border-collapse:collapse;width:100%}
.data-grid th,.data-grid td{border-right:1px solid var(--line);border-bottom:1px solid var(--line);text-align:left;padding-left:14px}
.data-grid th:last-child,.data-grid td:last-child{border-right:none}
.data-grid th{height:38px;background:var(--head-cell);font-weight:400;font-size:17px;color:var(--ink)}
.data-grid td{height:40px;font-size:14px;color:var(--text)}
.data-grid .check-col{padding-left:0;text-align:center;width:72px}
.box{display:inline-block;width:15px;height:15px;border:1px solid #9aa0a5;background:linear-gradient(#fff,#e6e8ea);vertical-align:middle}

.pager{height:58px;background:#f4f5f6;display:flex;align-items:center;padding:0 10px 0 15px;font-size:14px;color:var(--muted)}
.page-size{display:inline-block;width:36px;height:26px;background:#dde1e4;margin:0 10px 0 4px;position:relative;vertical-align:middle}
.page-size::after{content:"";position:absolute;left:12px;top:10px;border-left:6px solid transparent;border-right:6px solid transparent;border-top:8px solid #8a9096}
.pages{margin-left:auto;display:flex;align-items:center;height:36px;background:var(--white)}
.pg-btn{height:36px;padding:0 13px;background:var(--navy);color:var(--white);font-weight:700;font-size:14px;display:flex;align-items:center;border-radius:4px}
.pg-list{display:flex;align-items:center;padding:0 6px 0 30px;font-size:15px;color:var(--ink);gap:0}
.pg-list span{padding:0 6px;line-height:36px}
.pg-list .current{background:var(--chip);color:#fff;padding:0 8px}

.simple-table{position:absolute;left:304px;top:590px;width:416px;border:1px solid var(--line);background:var(--white)}
.simple-table th,.simple-table td{border-right:1px solid var(--line);border-bottom:1px solid var(--line);text-align:left;padding-left:14px}
.simple-table th:last-child,.simple-table td:last-child{border-right:none}
.simple-table tr:last-child td{border-bottom:none}
.simple-table th{height:40px;background:var(--head-cell);font-weight:400;font-size:17px;color:var(--ink)}
.simple-table td{height:36px;font-size:14px;color:var(--text)}
.simple-table tr.alt td{background:var(--stripe)}

.site-footer{position:absolute;left:0;top:888px;width:1200px;height:60px;background:var(--white);border-top:1px solid #e8eaec;display:flex;align-items:center;justify-content:space-between;padding:0 24px 0 14px;font-size:17px;color:var(--text)}
.footer-links span{margin:0 4px}
</style>
</head>
<body>
<header class="top-bar">
  <div class="brand"><div class="brand-dot"></div><div class="brand-name">VORELT</div></div>
  <div class="account">
    <div class="account-text"><div class="account-name">Lars Brenner</div><div class="account-role">Gest User</div></div>
    <div class="avatar" role="img" aria-label="User profile photo"></div>
    <div class="caret"></div>
  </div>
</header>

<nav class="side-nav">
  <div class="nav-item active"><svg viewBox="0 0 28 28"><path d="M4 20a10 10 0 1 1 20 0"/><path d="M14 20l5-6"/><path d="M4 22h20"/></svg>Dashboard</div>
  <div class="nav-item"><svg viewBox="0 0 28 28"><circle cx="14" cy="14" r="11"/><circle cx="14" cy="11" r="4"/><path d="M7 22c2-4 12-4 14 0"/></svg>Profile</div>
  <div class="nav-item"><svg viewBox="0 0 28 28"><circle cx="10" cy="10" r="5" stroke-dasharray="3 2" stroke-width="4"/><circle cx="20" cy="19" r="4" stroke-dasharray="2.5 1.5" stroke-width="3"/></svg>Settings</div>
  <div class="nav-item"><svg viewBox="0 0 28 28"><path d="M5 24V14M10 24V10M15 24V12M20 24V8M24 24V14M4 10l6-5 5 4 6-6 3 3"/></svg>Charts</div>
  <div class="nav-item"><svg viewBox="0 0 28 28"><path d="M4 6h5v4H4zM12 6h12v4H12zM4 12h5v4H4zM12 12h12v4H12zM4 18h5v4H4zM12 18h12v4H12z"/></svg>Forms</div>
  <div class="nav-item"><svg viewBox="0 0 28 28"><circle cx="14" cy="14" r="10"/><path d="M9 12l5 5 5-5"/></svg>Dropdown</div>
  <div class="nav-item plain"><svg viewBox="0 0 28 28"><path d="M20 15v7H6V8h7"/><path d="M16 6h6v6M22 6l-9 9"/></svg>Logout</div>
</nav>

<h2 class="section-title" style="top:186px">Grid Styling</h2>
<section class="data-grid">
  <table>
    <tr><th class="check-col"><span class="box"></span></th><th style="width:144px">Record</th><th style="width:120px">Batch ID</th><th style="width:204px">Keyword</th><th style="width:108px">Status</th><th>Reason</th></tr>
    <tr><td class="check-col"><span class="box"></span></td><td>Milan</td><td>Yes</td><td>Some Dummy Text</td><td>Rejected</td><td>Policy Error: (adult)</td></tr>
    <tr><td class="check-col"><span class="box"></span></td><td>Milan</td><td>Yes</td><td>Some Dummy Text</td><td>Rejected</td><td>Policy Error: (adult)</td></tr>
    <tr><td class="check-col"><span class="box"></span></td><td>Milan</td><td>Yes</td><td>Some Dummy Text</td><td>Rejected</td><td>Policy Error: (adult)</td></tr>
    <tr><td class="check-col"><span class="box"></span></td><td>Milan</td><td>Yes</td><td>Some Dummy Text</td><td>Rejected</td><td>Policy Error: (adult)</td></tr>
  </table>
  <div class="pager">
    Showing 1 to 10 of 21<span class="page-size"></span>rows records per page
    <div class="pages">
      <div class="pg-btn">FIRST</div>
      <div class="pg-list"><span class="current">1</span><span>2</span><span>3</span><span>4</span><span>5</span><span>6</span><span>7</span><span>8</span><span>9</span><span>10</span><span>....</span><span>100</span></div>
      <div class="pg-btn">LAST</div>
    </div>
  </div>
</section>

<h2 class="section-title" style="top:548px">Table Styling</h2>
<section class="simple-table">
  <table>
    <tr><th style="width:72px">ID</th><th style="width:204px">Name</th><th>Approved</th></tr>
    <tr><td>201</td><td>Milan</td><td>Yes</td></tr>
    <tr class="alt"><td>202</td><td>Oskar</td><td>No</td></tr>
    <tr><td>203</td><td>Rafael</td><td>Yes</td></tr>
    <tr class="alt"><td>204</td><td>Ivo</td><td>No</td></tr>
  </table>
</section>

<footer class="site-footer">
  <div>© 2016 VORELT. All rights reserved.</div>
  <div class="footer-links">Help <span>/</span> Disclaimer <span>/</span> Contact</div>
</footer>
</body>
</html>
```